Redesign of Simple Mobile App for Salesman

We want a redesign of an existing mobile app. The current app is very plain and basic. Salesman uses this app to quickly find and send information to customers while onsite.

https://apps.brelvano.com/store/apps/details?id=com.Vekarom

Target Market(s)

Internal Salesman

Industry/Entity Type

Chemical Coating

Colors

Designer to choose colors to be used in the design.

```html
<!DOCTYPE html>
<html lang="en">
<head>
<meta charset="utf-8">
<title>Vekarom – Literature</title>
<link href="https://fonts.googleapis.com/css2?family=Open+Sans:wght@400;600;700&display=swap" rel="stylesheet">
<style>
  :root {
    --bg-top: #1f4f98;
    --bg-bottom: #2a64b2;
    --panel-top: #1a92d8;
    --panel-bottom: #1d63b0;
    --tabbar: #1e4c94;
    --tabbar-line: #3c75c2;
    --button: #5b86c4;
    --white: #ffffff;
    --divider: rgba(255,255,255,0.22);
    --chevron: #2a6fb8;
  }
  * { margin: 0; padding: 0; box-sizing: border-box; }
  html, body { width: 675px; height: 1200px; overflow: hidden; }
  body {
    font-family: "Open Sans", Arial, sans-serif;
    color: var(--white);
    background: linear-gradient(180deg, var(--bg-top) 0%, var(--bg-bottom) 100%);
    position: relative;
  }
  .status-bar {
    position: absolute; top: 0; left: 0; right: 0; height: 50px;
    display: flex; align-items: center; justify-content: space-between;
    padding: 0 14px; font-size: 20px; font-weight: 400;
  }
  .status-left, .status-right { display: flex; align-items: center; gap: 8px; }
  .signal { display: flex; gap: 3px; }
  .signal span { width: 9px; height: 9px; border-radius: 50%; background: var(--white); }
  .signal span.empty { background: transparent; border: 1.5px solid var(--white); }
  .header-button {
    position: absolute; top: 97px; width: 62px; height: 43px;
    background: var(--button); border-radius: 4px;
    display: flex; align-items: center; justify-content: center;
  }
  .header-button.menu { left: 22px; }
  .header-button.settings { left: 590px; }
  .page-title {
    position: absolute; top: 102px; left: 0; right: 0; text-align: center;
    font-size: 20px; font-weight: 700; letter-spacing: 0.5px;
  }
  .literature-panel {
    position: absolute; left: 22px; top: 194px; width: 630px; height: 820px;
    background: linear-gradient(180deg, var(--panel-top) 0%, var(--panel-bottom) 70%, rgba(42,100,178,0) 100%);
  }
  .timeline {
    position: absolute; left: 38px; top: 71px; width: 2px; height: 385px;
    background: rgba(255,255,255,0.7);
  }
  .doc-item {
    position: absolute; left: 0; right: 0; height: 40px;
    display: flex; align-items: center;
  }
  .doc-item .dot {
    position: absolute; left: 30px; width: 18px; height: 18px;
    border-radius: 50%; background: var(--white);
  }
  .doc-item .label { position: absolute; left: 82px; font-size: 20px; font-weight: 400; }
  .doc-item .open {
    position: absolute; left: 542px; width: 46px; height: 46px;
    border-radius: 50%; background: var(--white);
    display: flex; align-items: center; justify-content: center;
  }
  .divider {
    position: absolute; left: 82px; right: 0; height: 1px; background: var(--divider);
  }
  .tab-bar {
    position: absolute; left: 0; right: 0; bottom: 0; height: 104px;
    background: var(--tabbar); border-top: 2px solid var(--tabbar-line);
  }
  .tab-icon { position: absolute; top: 32px; }
  .tab-center {
    position: absolute; left: 280px; top: -14px; width: 115px; height: 115px;
    border-radius: 50%; background: var(--tabbar); border: 2px solid var(--tabbar-line);
    display: flex; align-items: center; justify-content: center;
  }
  .tab-center .ring {
    width: 96px; height: 96px; border-radius: 50%; border: 3px solid var(--white);
    display: flex; align-items: center; justify-content: center;
  }
</style>
</head>
<body>
  <div class="status-bar">
    <div class="status-left">
      <div class="signal"><span></span><span></span><span></span><span></span><span class="empty"></span></div>
      <span>Carrier</span>
      <svg width="22" height="16" viewBox="0 0 22 16"><path d="M1 5a14 14 0 0 1 20 0M4.5 8.5a9 9 0 0 1 13 0M8 12a4 4 0 0 1 6 0" fill="none" stroke="#fff" stroke-width="2" stroke-linecap="round"/><circle cx="11" cy="14.5" r="1.5" fill="#fff"/></svg>
    </div>
    <div class="status-right">
      <svg width="18" height="18" viewBox="0 0 18 18"><circle cx="9" cy="9" r="7.5" fill="none" stroke="#fff" stroke-width="1.6"/><path d="M9 4.5v4.5l3 2" fill="none" stroke="#fff" stroke-width="1.6"/></svg>
      <span>100%</span>
      <svg width="44" height="20" viewBox="0 0 44 20"><rect x="1" y="1" width="38" height="18" rx="4" fill="none" stroke="#fff" stroke-width="1.6"/><rect x="4" y="4" width="32" height="12" rx="2" fill="#fff"/><rect x="40.5" y="7" width="2.5" height="6" rx="1" fill="#fff"/></svg>
    </div>
  </div>

  <div class="header-button menu" aria-label="Menu">
    <svg width="28" height="22" viewBox="0 0 28 22" fill="#fff"><circle cx="3" cy="3" r="2.4"/><circle cx="3" cy="11" r="2.4"/><circle cx="3" cy="19" r="2.4"/><rect x="8" y="1.5" width="20" height="3" rx="1"/><rect x="8" y="9.5" width="20" height="3" rx="1"/><rect x="8" y="17.5" width="20" height="3" rx="1"/></svg>
  </div>
  <h1 class="page-title">LITERATURE</h1>
  <div class="header-button settings" aria-label="Settings">
    <svg width="26" height="26" viewBox="0 0 24 24" fill="none" stroke="#fff" stroke-width="2"><circle cx="12" cy="12" r="3.2"/><path d="M12 2.5v3M12 18.5v3M2.5 12h3M18.5 12h3M5.3 5.3l2.1 2.1M16.6 16.6l2.1 2.1M5.3 18.7l2.1-2.1M16.6 7.4l2.1-2.1"/><circle cx="12" cy="12" r="6.5"/></svg>
  </div>

  <section class="literature-panel">
    <div class="timeline"></div>

    <div class="doc-item" style="top:51px"><span class="dot"></span><span class="label">Care Studies</span><span class="open"><svg width="14" height="22" viewBox="0 0 14 22"><path d="M3 3l8 8-8 8" fill="none" stroke="var(--chevron)" stroke-width="2.6" stroke-linecap="round" stroke-linejoin="round"/></svg></span></div>
    <div class="divider" style="top:134px"></div>

    <div class="doc-item" style="top:175px"><span class="dot"></span><span class="label">Coating Resins Reference Guide</span><span class="open"><svg width="14" height="22" viewBox="0 0 14 22"><path d="M3 3l8 8-8 8" fill="none" stroke="var(--chevron)" stroke-width="2.6" stroke-linecap="round" stroke-linejoin="round"/></svg></span></div>
    <div class="divider" style="top:258px"></div>

    <div class="doc-item" style="top:306px"><span class="dot"></span><span class="label">Composites Application Guide</span><span class="open"><svg width="14" height="22" viewBox="0 0 14 22"><path d="M3 3l8 8-8 8" fill="none" stroke="var(--chevron)" stroke-width="2.6" stroke-linecap="round" stroke-linejoin="round"/></svg></span></div>
    <div class="divider" style="top:396px"></div>

    <div class="doc-item" style="top:436px"><span class="dot"></span><span class="label">Product Line Guide</span><span class="open"><svg width="14" height="22" viewBox="0 0 14 22"><path d="M3 3l8 8-8 8" fill="none" stroke="var(--chevron)" stroke-width="2.6" stroke-linecap="round" stroke-linejoin="round"/></svg></span></div>
  </section>

  <nav class="tab-bar">
    <svg class="tab-icon" style="left:62px" width="38" height="30" viewBox="0 0 38 30" stroke="#fff" stroke-width="2.4" stroke-linecap="round"><path d="M2 4h34M2 15h34M2 26h34"/></svg>
    <svg class="tab-icon" style="left:180px" width="44" height="36" viewBox="0 0 44 36" fill="none" stroke="#fff" stroke-width="2"><circle cx="17" cy="11" r="8"/><path d="M2 34c0-8 7-13 15-13s15 5 15 13z"/><path d="M26 4a8 8 0 0 1 0 15M33 22c5 2 9 6 9 12h-7"/></svg>
    <div class="tab-center">
      <div class="ring">
        <svg width="36" height="48" viewBox="0 0 36 48" fill="none" stroke="#fff" stroke-width="2.8"><path d="M18 45S4 28 4 17a14 14 0 0 1 28 0c0 11-14 28-14 28z"/><circle cx="18" cy="17" r="5"/></svg>
      </div>
    </div>
    <svg class="tab-icon" style="left:462px" width="38" height="38" viewBox="0 0 38 38" fill="none" stroke="#fff" stroke-width="2"><rect x="2" y="5" width="34" height="31" rx="2"/><path d="M2 13h34M11 1v8M27 1v8"/><path d="M8 19h4M16 19h4M24 19h4M8 25h4M16 25h4M24 25h4M8 31h4M16 31h4" stroke-width="2.4"/></svg>
    <svg class="tab-icon" style="left:580px" width="38" height="38" viewBox="0 0 38 38" fill="none" stroke="#fff" stroke-width="2.4" stroke-linecap="round"><circle cx="16" cy="16" r="12"/><path d="M25 25l10 10"/></svg>
  </nav>
</body>
</html>
```